Webdesign für ambulanter Pflegedienst
Zielgruppe
Es ist ein ambulanter Pflegedienst, der sich im Raum Dessau-Roßlau um die Versorgung sowie Betreuung von Menschen kümmert. Kontaktdaten: ambulanter Pflegedienst Hand Sorge; Inhaberin: Sabine Lohmar; Birkenweg 14, 06871 Dessau-Roßlau Telefon: 034907/519364
IK-Nummer: 47 283 6194
e-mail: sl-hand-sorge@postfeld.de
Aufgabenstellung
Die Farben sollen in Anlehnung an das Logo sein, dass mit übersandt wird.

```html
<!DOCTYPE html>
<html lang="de">
<head>
<meta charset="utf-8">
<title>Hand Sorge – Ambulanter Pflegedienst</title>
<link href="https://fonts.googleapis.com/css2?family=Raleway:wght@400;500;600;700&family=Reenie+Beanie&display=swap" rel="stylesheet">
<style>
:root{
  --teal:#45aca9;
  --teal-dark:#3a9e9b;
  --green:#8bbd3c;
  --text:#5b5b5b;
  --heading:#5e5e5e;
  --sky:#dcedf7;
  --blob-green:#dceccb;
  --blob-blue:#d7ebf8;
  --white:#fff;
}
*{box-sizing:border-box;margin:0;padding:0}
html,body{width:1200px;height:3304px;overflow:hidden;background:var(--white)}
body{position:relative;font-family:"Raleway",sans-serif;color:var(--text)}
.abs{position:absolute}
.script{font-family:"Reenie Beanie",cursive;color:var(--heading)}
.rule{position:absolute;height:3px;width:98px;background:var(--green);border-radius:2px}

/* nav */
.nav{position:absolute;top:0;left:0;width:1200px;height:51px;background:var(--white)}
.brand{position:absolute;left:263px;top:14px;display:flex;align-items:center;gap:6px;font-size:11px;font-weight:600;color:var(--teal)}
.brand-dot{width:14px;height:14px;border-radius:50%;background:var(--teal)}
.nav-links{position:absolute;left:419px;top:18px;display:flex;gap:0;font-size:13px}
.nav-links a{text-decoration:none;color:var(--text);margin-right:32px}
.nav-links a.active{color:var(--green);font-weight:600}
.subbar{position:absolute;top:51px;left:0;width:1200px;height:26px;background:var(--sky);text-align:center;font-size:11px;line-height:26px;color:var(--text)}
.subbar b{color:var(--teal);font-weight:500}
.subbar span{font-family:"Reenie Beanie",cursive;font-size:15px}

/* hero */
.hero-title{position:absolute;left:589px;top:160px;font-size:52px;font-weight:700;line-height:56px;color:var(--heading)}
.hero-title em{font-style:normal;color:var(--teal)}
.hero-ask{position:absolute;left:594px;top:332px;font-size:24px}
.btn-ghost{position:absolute;top:378px;width:115px;height:43px;background:var(--white);border-radius:5px;box-shadow:0 2px 8px rgba(0,0,0,.14);color:var(--teal);font-size:11.5px;text-align:center;line-height:43px}
.hero-badge{position:absolute;left:142px;top:306px;width:144px;height:144px;border-radius:50%;background:var(--white);box-shadow:0 3px 12px rgba(0,0,0,.1);display:flex;flex-direction:column;align-items:center;justify-content:center;gap:8px;font-size:16px;font-weight:600;color:var(--heading)}
.badge-dot{width:26px;height:26px;border-radius:50%;background:var(--teal)}

/* intro */
.intro{position:absolute;left:0;top:552px;width:1200px;height:729px;background:linear-gradient(100deg,#f1f1e8 0%,#e2ece4 40%,#a9dbd8 100%)}
.center{text-align:center;width:1200px;left:0}
.eyebrow{font-size:22px}
.h2{font-size:29px;font-weight:700;line-height:32px;color:var(--heading)}
.h2 em{font-style:normal;color:var(--teal)}
.col{position:absolute;top:182px;width:326px;font-size:12.3px;line-height:15.6px;text-align:justify}
.col p+p{margin-top:15.6px}
.contact-card{position:absolute;left:290px;top:469px;width:621px;height:166px;background:var(--white);border-radius:4px;box-shadow:0 3px 12px rgba(0,0,0,.1)}
.contact-card .mark{position:absolute;left:30px;top:38px;width:90px;height:90px;border-radius:50%;border:3px solid var(--teal);display:flex;align-items:center;justify-content:center;font-size:13px;font-weight:600;color:var(--teal)}
.contact-card p{position:absolute;left:166px;top:38px;width:420px;font-size:12.3px;line-height:19px}
.link{color:var(--teal);font-weight:700;font-size:14px}

/* letter */
.letter-title{position:absolute;left:263px;top:1332px;font-size:36px}
.letter-text{position:absolute;left:263px;top:1398px;width:410px;font-size:12.3px;line-height:15.6px}
.letter-text p+p{margin-top:15.6px}
.signature{position:absolute;left:263px;top:1890px;font-size:22px}
.hello-card{position:absolute;left:707px;top:1536px;width:157px;height:142px;background:var(--white);border-radius:4px;box-shadow:0 3px 12px rgba(0,0,0,.12);padding:28px 22px;font-size:12px;line-height:14px}
.hello-card small{display:block;margin-top:16px;font-size:8px;line-height:9px;font-style:italic;color:#999}
.hello-card small b{color:#5ab6e0;font-weight:400}

/* services */
.card{position:absolute;top:2217px;width:205px;height:278px;background:var(--white);border-radius:4px;box-shadow:0 2px 10px rgba(0,0,0,.12);text-align:center}
.card h3{font-family:"Reenie Beanie",cursive;font-weight:400;font-size:22px;margin-top:66px;color:var(--heading)}
.card p{font-size:12.3px;line-height:19px;margin:18px 20px 0;height:96px}
.card .link{display:block;margin-top:22px}
.icon-circle{position:absolute;top:-48px;left:60px;width:85px;height:85px;border-radius:50%;background:linear-gradient(135deg,#f4f5ef,#a9dbd8);display:flex;align-items:center;justify-content:center}

/* courses */
.courses-text{position:absolute;top:2704px;left:340px;width:520px;text-align:center;font-size:12.3px;line-height:15.6px}
.btn-solid{position:absolute;left:511px;top:2790px;width:178px;height:46px;border-radius:23px;background:var(--teal);color:var(--white);font-size:12px;font-weight:700;text-align:center;line-height:46px}

/* footer */
.footer{position:absolute;top:3021px;left:0;width:1200px;height:238px;background:linear-gradient(90deg,#a9dbd8 0%,#cfe7e2 45%,#e9eee6 60%)}
.footer-photo{position:absolute;right:0;top:0;width:470px;height:238px;background:linear-gradient(90deg,rgba(233,238,230,0) 0%,#cfc3b6 35%,#8a6e5a 70%,#3c4b64 100%)}
.footer-title{position:absolute;left:263px;top:38px;font-size:26px}
.footer-info{position:absolute;left:263px;top:78px;font-size:12.3px;line-height:19px}
.footer-brand{position:absolute;left:520px;top:118px;width:160px;display:flex;flex-direction:column;align-items:center;gap:8px;font-size:17px;font-weight:600;color:var(--heading)}
.to-top{position:absolute;left:834px;top:2964px;width:103px;height:103px;border-radius:50%;background:var(--sky);text-align:center}
.to-top span{position:absolute;left:0;width:103px;top:58px;font-size:17px}
.bottom-bar{position:absolute;top:3259px;left:0;width:1200px;height:45px;background:var(--sky)}
.bottom-bar a{position:absolute;top:16px;font-size:10px;font-weight:700;color:var(--heading);text-decoration:none;letter-spacing:.3px}
.bottom-bar .copy{position:absolute;left:708px;top:17px;font-size:8.5px;color:#888}
</style>
</head>
<body>

<header class="nav">
  <div class="brand"><span class="brand-dot"></span>Hand Sorge</div>
  <nav class="nav-links">
    <a class="active">Startseite</a><a>Sofortige Hilfen</a><a>Unsere Leistungen</a><a>Karriere</a><a>Pflegekurse</a>
  </nav>
</header>
<div class="subbar"><b>Hand Sorge</b> – <span>Pflege von Mensch zu Mensch</span></div>

<!-- hero -->
<section class="hero">
  <svg class="abs" style="left:60px;top:77px" width="500" height="400" viewBox="0 0 500 400" aria-hidden="true">
    <path d="M40 70 C90 40 150 60 200 50 C300 30 420 30 470 130 C500 200 460 290 380 320 C300 350 220 330 160 340 C90 350 20 320 8 250 C-5 180 0 100 40 70Z" fill="var(--blob-green)"/>
    <circle cx="172" cy="375" r="12" fill="var(--blob-green)"/>
    <circle cx="145" cy="394" r="6" fill="var(--blob-green)"/>
  </svg>
  <div role="img" aria-label="Foto: Pflegerin mit Teetasse lächelt einen älteren Mann im Sessel an" class="abs" style="left:67px;top:77px;width:485px;height:345px;border-radius:48% 40% 45% 55% / 50% 40% 55% 50%;background:linear-gradient(120deg,#c9c0b2 0%,#e4e0d6 40%,#a7aea6 70%,#6d6a5e 100%)"></div>
  <div class="hero-badge"><span class="badge-dot"></span>HAND SORGE</div>

  <h1 class="hero-title">Wilkommen im<br><em>Hand Sorge</em></h1>
  <div class="rule" style="left:597px;top:295px"></div>
  <div class="hero-ask script">Wie können wir Ihnen helfen?</div>
  <svg class="abs" style="left:800px;top:334px" width="58" height="32" viewBox="0 0 58 32" fill="none" stroke="var(--green)" stroke-width="1.6" aria-hidden="true">
    <path d="M2 10 C18 0 42 2 50 26"/><path d="M43 20 L50 27 L55 19"/>
  </svg>
  <div class="btn-ghost" style="left:593px">Sofortige Hilfen</div>
  <div class="btn-ghost" style="left:716px">Alle Leistungen</div>
  <div class="btn-ghost" style="left:839px">Karriere bei uns</div>
</section>

<!-- intro -->
<section class="intro">
  <div class="abs center script eyebrow" style="top:36px">Der Mensch im Mittelpunkt</div>
  <h2 class="abs center h2" style="top:72px">Für uns ist Pflege eine<br><em>Herzensangelegenheit</em></h2>
  <div class="rule" style="left:551px;top:156px"></div>
  <div class="col" style="left:263px">
    <p>Für unseren ambulanten Pflegedienst steht die Pflege von Mensch zu Mensch im Mittelpunkt. Es ist unser Ziel, die Fähigkeiten und Möglichkeiten der Menschen zu erhalten und zu fördern, damit sie ihr Leben so lange wie möglich unabhängig führen und gestalten können. Damit den Pflegebedürftigen eine höchstmögliche Beständigkeit im gesamten Pflegeprozess gewährleistet werden kann, wird ihm eine Bezugsperson zugeordnet. Dies stärkt die Entwicklung von Vertrauen und ermöglicht so eine ganzheitliche Pflege.</p>
    <p>Es ist uns wichtig die Angehörigen aktiv in die Gestaltung der Pflege mit einzubeziehen. Dieses Vorhaben wird durch uns in Form von Beratungs-, Anleitungs- und Begleitungsangeboten realisiert.</p>
  </div>
  <div class="col" style="left:611px">
    <p>Eine interdisziplinäre Zusammenarbeit mit Thera&shy;peuten, Ärzten und anderen Dienstleistern (dazu gehören Sanitätshäuser, Apotheken, Ärzten und Wundschwestern) trägt zur Erhaltung, Förderung und gegebenenfalls Verbesserung der Lebenssituation des Pflegebedürftigen bei und wird durch uns angestrebt, unterstützt und koordiniert.<br>Unsere Mitarbeiter bilden die Verbindung zu den Pflegebedürftigen, den Angehörigen und den anderen Professionen und werden entsprechend ihrer Aufgaben sowie beruflichen Qualifikationen intern und extern weitergebildet, um eine höchstmögliche Qualität erreichen zu können. Mit diesem Komplettpaket möchten wir Sie unterstützen den Schicksalsschlag „Pflegebedürftigkeit“ gut bewältigen zu können.</p>
  </div>
  <div class="contact-card">
    <div class="mark">Hand Sorge</div>
    <p>Sollten Sie das Gefühl haben ein Angehöriger braucht Hilfe beziehungsweise Unterstützung? Kontaktieren Sie uns und wir schauen zusammen, wie wir eine Verbesserung der Lebenssituation erreichen können.</p>
    <div class="abs link" style="left:396px;top:126px">Jetzt Kontakt aufnehmen</div>
    <svg class="abs" style="left:581px;top:128px" width="10" height="16" viewBox="0 0 10 16" fill="none" stroke="var(--teal)" stroke-width="1.8"><path d="M2 2 L8 8 L2 14"/></svg>
  </div>
</section>

<!-- letter -->
<section class="letter">
  <svg class="abs" style="left:680px;top:1257px" width="330" height="350" viewBox="0 0 330 350" aria-hidden="true">
    <path d="M120 10 C200 -10 260 30 260 90 C270 150 340 200 318 270 C300 330 230 345 180 320 C120 290 60 280 25 230 C-10 180 0 100 40 60 C60 35 90 18 120 10Z" fill="var(--blob-blue)"/>
    <circle cx="301" cy="116" r="7" fill="var(--blob-blue)"/>
    <circle cx="304" cy="150" r="11" fill="var(--blob-blue)"/>
  </svg>
  <div role="img" aria-label="Schwarzweiß-Porträt der Inhaberin Sabine Lohmar" class="abs" style="left:730px;top:1307px;width:210px;height:295px;border-radius:50% 50% 20% 40% / 40% 40% 30% 30%;background:linear-gradient(160deg,#cfcfcf,#7d7d7d 60%,#2e2e2e)"></div>
  <svg class="abs" style="left:648px;top:1338px" width="80" height="40" viewBox="0 0 80 40" fill="none" stroke="var(--green)" stroke-width="1.6" aria-hidden="true">
    <path d="M78 32 C60 6 30 2 6 26"/><path d="M4 16 L5 28 L16 26"/>
  </svg>
  <h2 class="letter-title script">Liebe Patienten,</h2>
  <div class="rule" style="left:263px;top:1378px;background:var(--teal)"></div>
  <div class="letter-text">
    <p>von einem auf den anderen Tag kann sich schlagartig alles ändern. Ein Schicksalsschlag verändert ihr Leben und Sie benötigen dringend jemand, der sich um sie oder einen Familienangehörigen kümmert. Mit der Versorgung durch einen ambulanten Pflegedienst sind sie bei uns damit genau richtig. Unsere Motivation ist es Ihnen so lange wie möglich ein Leben in der eigenen Häuslichkeit zu ermöglichen. Des Weiteren steht im Mittelpunkt unserer Bemühungen stets der Mensch.</p>
    <p>Als Inhaberin / Pflegedienstleitung des ambulanten Pflegedienstes „Hand Sorge“ ist es für mich selbstverständlich mit gutem Beispiel voranzugehen. Daher habe ich mich seit meiner Ausbildung als Altenpflegefachkraft darum bemüht mein Wissen stetig zu erweitern. Zu meinen abgeschlossenen Weiterbildungen gehören unter anderem die Pflegedienstleitung, Stationsschwester, Heimleitung, Praxisanleiter / Mentor, Palliativ-schwester, Demenzfachkraft, Pflegeberaterin nach §7a SGB XI uvm. Aktuell arbeite ich an meinem Studium zum Bachelor of Science Pflege.</p>
    <p>Meines Erachtens ist der Schlüssel zu einer guten Pflege neben der Herzlichkeit, Empathie und Engagement, das nötige Wissen. Daher werden die Mitarbeiter unseres Pflegedienstes kontinuierlich intern und extern fortgebildet. So kann gewährleistet werden, dass sie kompetent agieren können. Den Angehörigen können wir dann mit Rat und Tat zur Seite stehen und ihnen einen erheblichen Teil der Belastungen abnehmen.</p>
    <p>Sie können sich gern selbst von unserem Pflegedienst überzeugen. Uns ist es wichtig, dass sie ein gutes Gefühl haben, denn nur dann können wir gemeinsam mit ihnen eine sehr gute Pflege gewährleisten.</p>
    <p>Ich freue mich auf eine gelungene Zusammenarbeit!</p>
  </div>
  <div class="signature script">Ihre Sabine Lohmar</div>
  <div class="hello-card">
    <svg class="abs" style="right:16px;top:16px" width="24" height="24" viewBox="0 0 24 24" fill="none" stroke="var(--teal)" stroke-width="1.4"><circle cx="12" cy="12" r="10"/><path d="M7 14 C9 17 15 17 17 14"/><path d="M8 9h2M14 9h2"/></svg>
    Hey, ich bin<br><b style="font-weight:600;color:#444">Sabine Lohmar.</b><br>Ich freue mich, Sie kennenzulernen.
    <small>Inhaberin des ambulanten Pflegedienstes <b>Hand Sorge</b></small>
  </div>
</section>

<!-- services -->
<section class="services">
  <div class="abs center script eyebrow" style="top:2012px">Alles aus einer Hand</div>
  <h2 class="abs center h2" style="top:2048px;font-size:28px">Was können wir<br>für Sie tun?</h2>
  <div class="rule" style="left:551px;top:2123px"></div>

  <div class="card" style="left:263px">
    <div class="icon-circle"><svg width="34" height="34" viewBox="0 0 34 34" fill="none" stroke="#555" stroke-width="1.4"><circle cx="17" cy="17" r="14"/><circle cx="17" cy="17" r="6"/><path d="M7 7l6 6M27 7l-6 6M7 27l6-6M27 27l-6-6"/></svg></div>
    <h3>Sofortige Hilfen</h3>
    <p>Ob Überleitungspflege oder individuelle Schulungen für pflegende Angehörige - wir sind Ihr kompetenter Ansprechpartner</p>
    <span class="link">Mehr dazu &nbsp;›</span>
  </div>
  <div class="card" style="left:498px">
    <div class="icon-circle"><svg width="44" height="34" viewBox="0 0 44 34" fill="none" stroke="#555" stroke-width="1.4"><path d="M4 22 C4 14 8 8 12 8 L14 20 M16 6 L17 20 M20 6 L20 20"/><path d="M40 22 C40 14 36 8 32 8 L30 20 M28 6 L27 20 M24 6 L24 20"/><path d="M2 22 C10 30 34 30 42 22"/><path d="M22 26 C18 22 17 19 19 18 C20.5 17 22 18.5 22 19.5 C22 18.5 23.5 17 25 18 C27 19 26 22 22 26Z" fill="#555"/></svg></div>
    <h3>Unsere Leistungen</h3>
    <p>Hier finden Sie eine detaillierte Auflistung unserer angebotenen Leistungen rund um den ambulanten Pflegedienst.</p>
    <span class="link">Mehr dazu &nbsp;›</span>
  </div>
  <div class="card" style="left:731px">
    <div class="icon-circle"><svg width="42" height="34" viewBox="0 0 42 34" fill="none" stroke="#555" stroke-width="1.4"><rect x="2" y="8" width="38" height="24" rx="3"/><path d="M15 8V4h12v4M2 18h38"/><rect x="17" y="15" width="8" height="6"/></svg></div>
    <h3>Karriere bei uns</h3>
    <p>Wir sind immer auf der Suche nach neuen Kollegen, die uns im alltäglichen Betrieb des ambulanten Pflegedienstes unterstützen.</p>
    <span class="link">Jetzt bewerben &nbsp;›</span>
  </div>
</section>

<!-- courses -->
<section class="courses">
  <div class="abs center script eyebrow" style="top:2583px">Unser Schulungsangebot für Sie</div>
  <h2 class="abs center h2" style="top:2620px;font-size:28px">Pflegekurse</h2>
  <p class="courses-text">Sie sind pflegende*r Angehörige*r und möchten lernen, besser mit der Erkrankung der/des Pflegebedürftige*n umzugehen und die Pflege allgemein effektiver und belastungarmer zu gestalten? Dann sind Sie bei uns genau richtig.</p>
  <div class="btn-solid">Pflegekurs buchen</div>
</section>

<!-- footer -->
<footer>
  <div class="footer">
    <div class="footer-photo" role="img" aria-label="Foto: gefaltete Hände einer älteren Person, gehalten von jüngeren Händen"></div>
    <div class="footer-title script">Wir sind für Sie da!</div>
    <div class="footer-info">
      ambulanter Pflegedienst Hand Sorge<br>Inhaberin: Sabine Lohmar<br>Birkenweg 14<br>06871 Dessau-Roßlau<br><span style="display:block;height:10px"></span>034907/519364<br>sl-hand-sorge@postfeld.de
    </div>
    <div class="footer-brand" style="top:82px"><span class="badge-dot" style="width:40px;height:40px"></span>HAND SORGE</div>
  </div>
  <div class="to-top">
    <svg class="abs" style="left:43px;top:22px" width="18" height="32" viewBox="0 0 18 32" fill="var(--green)"><path d="M9 0 L18 12 H12 V32 H6 V12 H0Z"/></svg>
    <span class="script">Nach oben</span>
  </div>
  <div class="bottom-bar">
    <a style="left:276px">KARRIERE</a>
    <a style="left:371px">KONTAKT</a>
    <a style="left:471px">DATENSCHUTZ</a>
    <a style="left:598px">IMPRESSUM</a>
    <span class="copy">Copyright 2023 © ambulanter Pflegedienst Hand Sorge</span>
  </div>
</footer>

</body>
</html>
```